Brennick Setter Club - Rare dog breed club needs web design!

The Transylvanian Hound (or Erdélyi kopó) is an ancient Hungarian dog breed. These medium-sized hounds were favored by the Hungarian kings and princes for hunting bears and wolves in the Carpathian mountains of Transylvania. The breed's great adaptability to the region's extreme climates of sweltering summers and frigid winters made it an excellent all season hunting dog. This dog has a sleek appearance and stunning good looks. They are lean, appear very elegant and proud. Their erect posture and beautifully sculpted head portray great attentiveness and authority. In general, this rare breed is extremely good natured, loyal and obedient. It has a tendency to form strong attachments to its primary caretakers and will remain loyal and protective. (Please refer to existing web resources.)

The Brennick Setter Club - with current website www.brennicksetter.com - is the official breed club of Transylvanian Hound afficionados, breeders and owners in the United States, which was founded in 2010. We are looking for a web design for the new, upgraded version of this central (currenty non-functioning) website. Please do not recycle the old logo (we may choose from your suggesions and pay for it!) or any of the old texts. Please use the structure described below. Overall, the webpage serves a dual purpose: an educational one (about the breed itself) and a community-building one (inside the Club). The proposed structure of the website is as follows:

1. About the Kopó
- Breed History
- Breed Standard
- Public Education
- Photo Gallery

2. Life with a Kopó
- Health and Genetics
- Feeding and Nutrition
- Training and Activities

3. Finding a Kopó
- Is this the Right Breed for You?
- Choosing a Puppy
- FAQ
- Breeder Referral

4. The Brennick Setter Club
- Constituton
- Officers and Appointees
- Code of Ethics
- Breeder Guidelines
- Membership
- Reports
- Links

5. News and Events

6. Shop

We are attaching a couple of examples of the graphics/drawings of the dogs that would be part of the design of the website. We plan to have more of these artistic depictions, nicely embedded into the background (maybe shaded out at the edges just like the drawings themselves) and less actual photos. Or a good combination of the two.

Further information upon request.

Reason: There are a few very promising design collaborations ongoing. As we moved the brief to a more artistic and graphic direction, we felt that one week of extension would be needed to get to the perfect end-product, which could include designs for sub-pages as well.

Reason: In order to make the final modifications to the leading designs, and at the request of those designers, the deadline is extended until Friday.

Target Market(s)

- BRSC Club members, dog (especially T-Hound) owners, past and future owners, breeders, puppy buyers, hunters, kennel clubs, dog show participants, vets, animal shelters, Hungarian, Romanian and other European web visitors, historians

Industry/Entity Type

Club

Font styles to use
Serif
Decorative
Script

Requirements
Must have
• - Sync with graphics of dogs (see attachments), but accentuate the rich black basic color of the dogs
- Elegance, aristocratic/noble look and feel (but not overly archaic)
- Love, companionship, dogs as family members
- Hunting usage, but no bloody associations, rather romantic ones
- Simple to use and navigate for non-web-natives
- Old world (Central European) atmosphere, even the exotic, rustic and romantic Transylvanian feel - SEE the new attachment for inspiration (this was a design plan which we discarded (mainly because of its gothic, (nazi-like), unreadable font, and the fact that the plan makes the black-looking dogs appear brown), however we loved the fact that it was not full of boxes/windows, had a marble/sand stone like continuous background, lots of little elegant graphics, the drawings embedded, etc.
Nice to have
• - Working on smartphone, Zentabs, etc., so dynamic website design
- Web shop to be added to functionalities in the future (?)
- English language for now, in the future can be Hungarian, Romanian, etc., so the font choice should handle various alphabets
- Focus on the dogs (likely more graphics than photos, at least on the main pages), and not on the activities/humans - the design should accentuate the black and not the tan of the graphics!
Should not have
• - Old logo from the old www.brennicksetter.com webpage or the other logo from the Chatterly site of the Brennick Setter Club, we will have a new one (maybe designed by you!)
- Breed club, kennel club cliches
- Cutesy, adorable, cheesy design elements
- Old, stale, monolithic, archaic, snobbish, etc. look and feel
- No vampire associations

```html
<!DOCTYPE html>
<html lang="en">
<head>
<meta charset="utf-8">
<title>Brennick Setter Club</title>
<link rel="stylesheet" href="https://fonts.googleapis.com/css2?family=EB+Garamond:ital,wght@0,400;0,500;1,400&family=Mrs+Saint+Delafield&family=Herr+Von+Muellerhoff&display=swap">
<style>
:root{
  --board:#3a3a3c;
  --page:#efebe9;
  --page-shade:#e6e1de;
  --ink:#2b2522;
  --ink-soft:#5c534e;
  --rule:#b7afaa;
  --paper:#eadcbf;
  --paper-edge:#d9c39a;
  --field:#dedad8;
  --dog-dark:#2a2420;
  --dog-tan:#8a5a34;
}
*{margin:0;padding:0;box-sizing:border-box}
html,body{width:877px;height:1200px;overflow:hidden;background:var(--board)}
body{position:relative;font-family:"EB Garamond",Georgia,serif;color:var(--ink)}
.page{position:absolute;background:linear-gradient(180deg,var(--page),var(--page-shade) 50%,var(--page));overflow:hidden}
.page--top{left:8px;top:0;width:426px;height:1200px}
.page--bottom{left:444px;top:70px;width:427px;height:1130px}
.abs{position:absolute}
.rule{position:absolute;left:0;right:0;border-top:1px dashed var(--rule)}
.script{font-family:"Mrs Saint Delafield",cursive;font-weight:400;color:var(--ink)}

/* header */
.brand{left:0;right:0;top:26px;text-align:center;font-size:19px;letter-spacing:1px;color:var(--ink);line-height:22px;text-transform:uppercase}
.brand small{display:block;font-size:14px;letter-spacing:2px}
.brand-dot{display:inline-block;width:8px;height:8px;border-radius:50%;background:var(--ink-soft);margin-right:8px;vertical-align:middle}
.nav{left:0;right:0;top:117px;text-align:center;font-size:13px;line-height:21px}
.nav a{color:var(--ink);text-decoration:underline;margin:0 4px}

/* welcome */
.welcome-pre{left:68px;top:205px;font-size:16px}
.welcome-title{left:14px;top:222px;font-size:52px;line-height:60px;white-space:nowrap}
.intro{left:12px;top:296px;width:410px;font-size:12.5px;line-height:15.5px}
.intro p{margin-bottom:15px}
.intro p.narrow{width:262px}

/* illustrations */
.art{position:absolute}
.art--head{left:258px;top:278px;width:166px;height:140px;background:radial-gradient(ellipse at 50% 45%,var(--dog-dark) 0%,#4a3a2e 40%,rgba(138,90,52,.35) 62%,rgba(239,235,233,0) 72%)}
.art--story{left:42px;top:596px;width:320px;height:140px;background:radial-gradient(ellipse at 35% 50%,var(--dog-dark) 0%,#3f342c 38%,rgba(120,90,70,.35) 62%,rgba(239,235,233,0) 74%)}
.art--lying{left:26px;top:775px;width:320px;height:130px;background:radial-gradient(ellipse at 50% 50%,var(--dog-dark) 0%,#4b3a2d 36%,rgba(138,90,52,.3) 60%,rgba(239,235,233,0) 72%)}

/* story card */
.card{position:absolute;width:300px;height:256px;transform:rotate(-3deg);background:linear-gradient(160deg,#f1e6cd,var(--paper) 60%,var(--paper-edge));padding:14px 16px 10px 18px;box-shadow:0 1px 3px rgba(0,0,0,.15)}
.card--main{left:68px;top:712px}
.card--echo{left:86px;top:30px}
.card h3{font-size:38px;line-height:34px;margin-bottom:2px}
.card p{font-size:10px;line-height:12.4px;margin-bottom:8px;color:#3a302a}
.card .sign{position:absolute;right:18px;bottom:10px;font-family:"Herr Von Muellerhoff",cursive;font-size:22px;line-height:24px;color:#3a302a}

.more{font-size:11px;font-style:italic;text-decoration:underline;color:var(--ink)}
.more::before{content:"";display:inline-block;width:12px;height:6px;border:1px solid var(--ink-soft);border-radius:50%;margin-right:5px;vertical-align:middle}

/* news */
.section-title{font-size:38px;line-height:46px;white-space:nowrap}
.section-title--contact{font-size:34px}
.news{position:absolute;left:0;right:0}
.news-date{position:absolute;left:18px;top:16px;width:30px;text-align:center;font-size:12px;color:var(--ink-soft)}
.news-date b{display:block;font-weight:400;font-size:18px;border-top:1px solid var(--ink-soft);margin-top:4px;padding-top:2px;color:var(--ink)}
.news-bar{position:absolute;left:55px;top:0;height:70px;border-left:1px solid var(--ink-soft)}
.news-text{position:absolute;left:74px;right:16px;top:0;font-size:12.8px;line-height:16.3px}
.news-sep{position:absolute;left:18px;right:18px;border-top:1px solid #c9c2be}

/* contact */
.form{left:18px;right:18px;top:900px;font-size:8.5px;color:var(--ink-soft)}
.field{height:20px;border-bottom:1px solid #d3cdc9;padding-top:6px}
.message{margin-top:10px;height:60px;background:var(--field);padding:8px 8px}
.footer{left:0;right:0;top:1094px;text-align:center;font-size:8.5px;line-height:11px;color:var(--ink-soft)}

/* fades */
.fade{position:absolute;left:0;right:0;pointer-events:none}
.fade--bottom{top:1010px;height:190px;background:linear-gradient(180deg,rgba(58,58,60,0),rgba(58,58,60,.55) 55%,rgba(58,58,60,.95))}
.fade--top{top:0;height:210px;background:linear-gradient(180deg,rgba(58,58,60,1),rgba(58,58,60,.55) 45%,rgba(58,58,60,0))}
</style>
</head>
<body>

<section class="page page--top">
  <div class="abs brand"><span class="brand-dot"></span>Brennick Setter<small>Club</small></div>
  <div class="rule" style="top:97px"></div>
  <nav class="abs nav">
    <a href="#">About the Kopó</a><a href="#">Life with a Kopó</a><a href="#">Finding a Kopó</a><br>
    <a href="#">The Brennick Setter Club</a><a href="#">News &amp; Events</a><a href="#">Shop</a>
  </nav>
  <div class="rule" style="top:180px"></div>

  <div class="abs welcome-pre">Welcome to the</div>
  <h1 class="abs script welcome-title">Brennick Setter Club</h1>
  <div class="art art--head" role="img" aria-label="Drawing of a black and tan hound's head"></div>
  <div class="abs intro">
    <p class="narrow">By building this website, our aim is to create a virtual forum to everyone who wishes to know more about Transylvanian Hounds, and would like to join us in expanding their popularity and number in the US.</p>
    <p class="narrow">It is really important to us to have the Transylvanian Hound registered with NCR, this way more and more people can be introduced to this historical breed.</p>
    <p>The breed registration is a long procedure, and we are inviting all Transylvanian Hound owners to register and sign up with us. This way, we can have the breed recognized by NCR quicker.</p>
    <p>Since this is a constantly developing website, we are greatly appreciate your advice, opinion, pictures, and stories that could help us create a well functioning interactive Brennick Setter Club.</p>
  </div>
  <div class="rule" style="top:583px"></div>

  <div class="art art--story" role="img" aria-label="Drawing of a black and tan hound resting over the story card"></div>
  <article class="card card--main">
    <h3 class="script">Vitéz</h3>
    <p>I was fortunate enough to be able to bring my first Transylvanian Hound puppy, Vitéz, home with me from Hungary. Learning the noble history and the danger of vanishing of this breed, strengthened my desire to help revive and popularize the Transylvanian Hound in the United States. Being a Transylvanian-Hungarian decent myself, I felt their "story" even more touching.</p>
    <p>Vitéz is a real character and the funniest beloved member of our family. He is a quick learner and has a friendly, people pleaser personality. He is already passed all levels of obedience classes and now preparing for the NCR Good Citizen test and his first Conformation Show with the Continental Rare Breed Society (CRBS).</p>
    <span class="sign">Ilka Varga</span>
  </article>
  <a class="abs more" href="#" style="left:258px;top:990px">Read More Stories</a>
  <div class="rule" style="top:1022px"></div>

  <h2 class="abs script section-title" style="left:90px;top:1046px">Latest News &amp; Events</h2>
  <div class="news" style="top:1112px">
    <div class="news-date">Jan<b>14</b></div>
    <div class="news-bar"></div>
    <p class="news-text">Lorem ipsum dolor sit amet, consectetur adipisicing elit, sed do eiusmod tempor incididunt ut labore et dolore magna aliqua. Ut enim ad minim veniam, quis nostrud exercitation ullamco laboris nisi ut aliquip ex ea commodo consequat. Duis aute irure dolor in reprehenderit in voluptate velit esse cillum dolore eu fugiat nulla</p>
  </div>
  <div class="fade fade--bottom"></div>
</section>

<section class="page page--bottom">
  <article class="card card--echo" aria-hidden="true">
    <h3 class="script">Vitéz</h3>
    <p>I was fortunate enough to be able to bring my first Transylvanian Hound puppy, Vitéz, home with me from Hungary. Learning the noble history and the danger of vanishing of this breed, strengthened my desire to help revive and popularize the Transylvanian Hound in the United States. Being a Transylvanian-Hungarian decent myself, I felt their "story" even more touching.</p>
    <p>Vitéz is a real character and the funniest beloved member of our family. He is a quick learner and has a friendly, people pleaser personality. He is already passed all levels of obedience classes and now preparing for the NCR Good Citizen test and his first Conformation Show with the Continental Rare Breed Society (CRBS).</p>
    <span class="sign">Ilka Varga</span>
  </article>
  <div class="fade fade--top"></div>
  <a class="abs more" href="#" style="left:258px;top:304px">Read More Stories</a>
  <div class="rule" style="top:340px"></div>

  <h2 class="abs script section-title" style="left:84px;top:366px">Latest News &amp; Events</h2>

  <div class="news" style="top:425px">
    <div class="news-date">Jan<b>14</b></div><div class="news-bar"></div>
    <p class="news-text">Lorem ipsum dolor sit amet, consectetur adipisicing elit, sed do eiusmod tempor incididunt ut labore et dolore magna aliqua. Ut enim ad minim veniam, quis nostrud exercitation ullamco laboris nisi ut aliquip ex ea commodo consequat. Duis aute irure dolor in reprehenderit in voluptate velit esse cillum dolore eu fugiat nulla</p>
  </div>
  <div class="news-sep" style="top:516px"></div>
  <div class="news" style="top:535px">
    <div class="news-date">Jan<b>14</b></div><div class="news-bar"></div>
    <p class="news-text">Lorem ipsum dolor sit amet, consectetur adipisicing elit, sed do eiusmod tempor incididunt ut labore et dolore magna aliqua. Ut enim ad minim veniam, quis nostrud exercitation ullamco laboris nisi ut aliquip ex ea commodo consequat. Duis aute irure dolor in reprehenderit in voluptate velit esse cillum dolore eu fugiat</p>
  </div>
  <div class="news-sep" style="top:623px"></div>
  <div class="news" style="top:642px">
    <div class="news-date">Jan<b>14</b></div><div class="news-bar"></div>
    <p class="news-text">Lorem ipsum dolor sit amet, consectetur adipisicing elit, sed do eiusmod tempor incididunt ut labore et dolore magna aliqua. Ut enim ad minim veniam, quis nostrud exercitation ullamco laboris nisi ut aliquip ex ea commodo consequat. Duis aute irure dolor in reprehenderit in voluptate velit esse cillum dolore eu fugiat</p>
  </div>
  <div class="news-sep" style="top:732px"></div>
  <a class="abs more" href="#" style="left:195px;top:742px">More News &amp; Events</a>
  <div class="rule" style="top:793px"></div>

  <div class="art art--lying" role="img" aria-label="Drawing of a black and tan hound lying down"></div>
  <h2 class="abs script section-title section-title--contact" style="left:278px;top:812px">Contact Us</h2>

  <form class="abs form">
    <div class="field">Name</div>
    <div class="field">E-mail</div>
    <div class="field">Web</div>
    <div class="message">Message</div>
  </form>
  <div class="rule" style="top:1080px"></div>
  <div class="abs footer">Brennick Setter Club<br>-Est 2010-</div>
</section>

</body>
</html>
```